Lumora business card for a plastic surgeon

we need a business card for plastic surgeons that work on a clinic called LUMORA.
we want a clean design and the following informations: name of the doctor, doctor's registration number (called CRM), telephone, address, facebook, instagram.
Colors: white, blue tones, light brown/ coffee

facebook and instagram: lumoracirurgiaestetica

Industry/Entity Type

Business

Contact Information for Business Card

clean design

Font styles to use
Serif
Sans Serif
Other font styles liked:
• helvetica light

Colors
cee9f5
85cae6
85abd2
3276b5
cfeae6
cedeed
eaf1f7

Requirements
Must have
• doctor's name
• identification number (called CRM)
• contact (phone, facebook, instagram, address)

```html
<!DOCTYPE html>
<html lang="pt">
<head>
<meta charset="utf-8">
<title>Lumora – Business Card</title>
<link rel="stylesheet" href="https://fonts.googleapis.com/css2?family=Crimson+Text:wght@400;600&display=swap">
<style>
  :root {
    --stage: #2e2b29;
    --card: #ffffff;
    --card-shade: #eceeef;
    --teal: #2aa9c6;
    --teal-soft: #5dbcd2;
    --navy: #1f4f86;
    --ink: #4a4a4a;
    --muted: #6a6a6a;
  }
  * { box-sizing: border-box; margin: 0; padding: 0; }
  html, body {
    width: 1200px; height: 950px; overflow: hidden;
    background: var(--stage);
  }
  .stage {
    width: 1200px; height: 950px;
    display: flex; flex-direction: column;
    align-items: center; justify-content: center; gap: 40px;
  }
  .card {
    position: relative;
    width: 760px; height: 434px;
    background: linear-gradient(135deg, var(--card) 55%, var(--card-shade) 100%);
    font-family: "Crimson Text", Georgia, serif;
    overflow: hidden;
  }

  /* Logo side */
  .card--brand {
    display: flex; flex-direction: column;
    align-items: center; justify-content: center;
  }
  .brand-name {
    font-size: 104px; font-weight: 400; letter-spacing: 6px;
    color: var(--teal); line-height: 1;
  }
  .brand-tagline {
    margin-top: 6px;
    font-size: 34px; letter-spacing: 4px;
    color: var(--navy); text-transform: uppercase;
  }
  .brand-social {
    margin-top: 34px;
    display: flex; align-items: center; gap: 10px;
    font-size: 24px; color: var(--ink);
  }
  .brand-social .dot {
    width: 22px; height: 22px; border-radius: 50%;
    background: var(--teal);
  }

  /* Contact side */
  .card--contact { padding: 48px 0 0 56px; }
  .doctor-name {
    font-size: 36px; color: var(--teal); line-height: 1.1;
  }
  .doctor-crm {
    font-size: 26px; font-weight: 600; color: var(--navy);
    letter-spacing: 1px;
  }
  .contact-list {
    list-style: none;
    margin-top: 64px;
    font-size: 24px; color: var(--ink); line-height: 1.2;
  }
  .contact-list li { display: flex; align-items: center; gap: 12px; }
  .contact-list .address { padding-left: 0; }
  .contact-list svg { width: 20px; height: 20px; flex: none; fill: var(--teal); }
  .rule {
    position: absolute; left: 0; bottom: 56px;
    width: 600px; height: 2px; background: var(--teal-soft);
  }
</style>
</head>
<body>
<main class="stage">

  <section class="card card--brand" aria-label="Lumora card, logo side">
    <h1 class="brand-name">LUMORA</h1>
    <p class="brand-tagline">Cirurgia Plástica</p>
    <p class="brand-social"><span class="dot" aria-hidden="true"></span>lumoracirurgiaestetica</p>
  </section>

  <section class="card card--contact" aria-label="Lumora card, contact side">
    <h2 class="doctor-name">Rafael Moura</h2>
    <p class="doctor-crm">(CRM)61392</p>
    <ul class="contact-list">
      <li class="address">2710 Alder Crest Road</li>
      <li class="address">Linden Vale, NY 10488</li>
      <li>
        <svg viewBox="0 0 20 20" aria-hidden="true"><path d="M4 2h4l1.5 4-2.2 1.5a10 10 0 0 0 5.2 5.2L14 10.5l4 1.5v4a2 2 0 0 1-2 2A14 14 0 0 1 2 4a2 2 0 0 1 2-2z"/></svg>
        555 0142 7781
      </li>
      <li>
        <svg viewBox="0 0 20 20" aria-hidden="true"><path d="M2 4h16v12H2z M2 4l8 6 8-6" stroke="#fff" stroke-width="1.4"/></svg>
        rafael@lumoraclinic.com
      </li>
      <li>
        <svg viewBox="0 0 20 20" aria-hidden="true"><circle cx="10" cy="10" r="8"/><path d="M2 10h16M10 2c3 3 3 13 0 16M10 2c-3 3-3 13 0 16" stroke="#fff" stroke-width="1.2" fill="none"/></svg>
        www.lumoraclinic.com
      </li>
    </ul>
    <div class="rule" aria-hidden="true"></div>
  </section>

</main>
</body>
</html>
```